Yard sign

I want it to look similar to this one,

change name to DRAVEK and submit new ideas

Also would like to improvise a bit. let's not make exactly the same thing

would like to change to: Connecticut #1 Company

also change phone to 203-555-0147
and website to
dravekllc.com

this is yard sign. size is 24' Width and 32' Height

Target Market(s)

Roof

Industry/Entity Type

Roofing

Requirements
Must have
• similar colors or add something new

```html
<!DOCTYPE html>
<html lang="en">
<head>
<meta charset="utf-8">
<title>Dravek Roofing Yard Sign</title>
<link rel="stylesheet" href="https://fonts.googleapis.com/css2?family=Cinzel:wght@400;500;600&family=Montserrat:wght@400;600;700&display=swap">
<style>
  :root {
    --sign-dark-top: #303336;
    --sign-dark-mid: #1d1f22;
    --sign-dark-bottom: #040405;
    --headline: #d9d9d9;
    --brand-amber: #f8bb58;
    --band-top: #9aa0a6;
    --band-bottom: #878c93;
    --phone-white: #ffffff;
    --web-text: #d6d6d6;
  }
  html, body {
    margin: 0;
    padding: 0;
    width: 835px;
    height: 1200px;
    overflow: hidden;
    background: var(--sign-dark-bottom);
  }
  .yard-sign {
    display: block;
    width: 835px;
    height: 1200px;
  }
  .headline {
    font-family: "Cinzel", serif;
    font-weight: 500;
    fill: var(--headline);
  }
  .brand-name {
    font-family: "Montserrat", sans-serif;
    font-weight: 600;
    fill: var(--brand-amber);
  }
  .tagline {
    font-family: "Cinzel", serif;
    font-weight: 600;
    fill: var(--headline);
  }
  .phone {
    font-family: "Montserrat", sans-serif;
    font-weight: 700;
    fill: var(--phone-white);
  }
  .website {
    font-family: "Montserrat", sans-serif;
    font-weight: 400;
    fill: var(--web-text);
  }
  .accent-rule {
    stroke: var(--brand-amber);
    stroke-width: 3;
  }
  .accent-strip {
    fill: var(--brand-amber);
  }
</style>
</head>
<body>
<svg class="yard-sign" viewBox="0 0 835 1200" xmlns="http://www.w3.org/2000/svg">
  <defs>
    <linearGradient id="sign-bg" x1="0" y1="0" x2="1" y2="1">
      <stop offset="0" stop-color="var(--sign-dark-top)"/>
      <stop offset="0.45" stop-color="var(--sign-dark-mid)"/>
      <stop offset="1" stop-color="var(--sign-dark-bottom)"/>
    </linearGradient>
    <linearGradient id="phone-band-bg" x1="0" y1="0" x2="0" y2="1">
      <stop offset="0" stop-color="var(--band-top)"/>
      <stop offset="1" stop-color="var(--band-bottom)"/>
    </linearGradient>
  </defs>

  <rect class="sign-background" x="0" y="0" width="835" height="1200" fill="url(#sign-bg)"/>

  <text class="headline" x="93" y="142" font-size="56" textLength="658" lengthAdjust="spacing">CONNECTICUT #1</text>
  <line class="accent-rule" x1="70" y1="194" x2="230" y2="194"/>
  <text class="headline" x="417.5" y="213" font-size="56" text-anchor="middle" textLength="330" lengthAdjust="spacing">COMPANY</text>
  <line class="accent-rule" x1="605" y1="194" x2="765" y2="194"/>

  <text class="brand-name" x="35" y="519" font-size="214" textLength="780" lengthAdjust="spacingAndGlyphs">DRAVEK</text>

  <text class="tagline" x="115" y="603" font-size="46" textLength="605" lengthAdjust="spacing">QUALITY YOU CAN TRUST</text>

  <rect class="accent-strip" x="0" y="759" width="835" height="8"/>
  <rect class="phone-band" x="0" y="767" width="835" height="153" fill="url(#phone-band-bg)"/>
  <rect class="accent-strip" x="0" y="920" width="835" height="8"/>
  <text class="phone" x="92" y="880" font-size="96" textLength="647" lengthAdjust="spacingAndGlyphs">203-555-0147</text>

  <text class="website" x="121" y="1148" font-size="30" textLength="614" lengthAdjust="spacing">WWW.DRAVEKLLC.COM</text>
</svg>
</body>
</html>
```